Plumbing Van Vehicle Signage

I need a design for vehicle signage for a group of plumbing vans. The company name is 'Brackenvale Gas & Plumbing'. I do all types of plumbing and gas fitting but specialise in general maintenance plumbing and gas fitting.

Industry/Entity Type

Plumbing

Requirements
Must have
• Must be eye catching. Must be able to go on a white back ground as the vans are white. Must contain phone number

```html
<!DOCTYPE html>
<html lang="en">
<head>
<meta charset="utf-8">
<title>Brackenvale Gas &amp; Plumbing – Van Signage</title>
<link href="https://fonts.googleapis.com/css2?family=Montserrat:wght@700;800&family=Open+Sans:wght@700&display=swap" rel="stylesheet">
<style>
  :root {
    --page: #eceef1;
    --van-white: #ffffff;
    --brand-blue: #1f5fb8;
    --charcoal: #333537;
    --band-dark: #2f3133;
    --orange-top: #f7b21e;
    --orange-bottom: #ef5a1c;
    --rule-orange: #f08a1c;
    --url-white: #ffffff;
  }
  * { margin: 0; padding: 0; box-sizing: border-box; }
  html, body { width: 1200px; height: 1200px; overflow: hidden; background: var(--page); }
  .canvas { position: relative; width: 1200px; height: 1200px; }
  .wrap-panel { position: absolute; display: block; filter: drop-shadow(0 4px 10px rgba(0,0,0,.12)); }
  .wrap-panel--kerb { left: 150px; top: 40px; width: 900px; height: 320px; }
  .wrap-panel--driver { left: 150px; top: 400px; width: 900px; height: 320px; }
  .wrap-panel--rear { left: 390px; top: 760px; width: 420px; height: 400px; }
  .phone { font-family: "Montserrat", sans-serif; font-weight: 800; fill: var(--charcoal); }
  .brand-name { font-family: "Montserrat", sans-serif; font-weight: 800; fill: var(--brand-blue); }
  .brand-sub { font-family: "Montserrat", sans-serif; font-weight: 800; fill: var(--brand-blue); }
  .web-address { font-family: "Open Sans", sans-serif; font-weight: 700; fill: var(--url-white); }
  .panel-body { fill: var(--van-white); }
  .band { fill: var(--band-dark); }
  .brand-dot { fill: var(--rule-orange); }
  .rule { stroke: var(--rule-orange); stroke-width: 4; }
  .stop-top { stop-color: var(--orange-top); }
  .stop-bottom { stop-color: var(--orange-bottom); }
</style>
</head>
<body>
<div class="canvas">

  <!-- Passenger side, front to the right -->
  <svg class="wrap-panel wrap-panel--kerb" viewBox="0 0 900 320" role="img" aria-label="Passenger side van panel layout">
    <defs>
      <linearGradient id="orange-fade-kerb" x1="0" y1="0" x2="0" y2="1">
        <stop offset="0" class="stop-top"/>
        <stop offset="1" class="stop-bottom"/>
      </linearGradient>
    </defs>
    <rect class="panel-body" x="0" y="0" width="900" height="320" rx="18"/>
    <path d="M0 175 L900 250 L900 302 Q900 320 882 320 L18 320 Q0 320 0 302 Z" fill="url(#orange-fade-kerb)"/>
    <path class="band" d="M0 140 L900 215 L900 250 L0 175 Z"/>
    <g transform="translate(0 157.5) rotate(4.76)">
      <circle class="brand-dot" cx="215" cy="-62" r="40"/>
      <text class="phone" x="285" y="-102" font-size="30" textLength="210" lengthAdjust="spacingAndGlyphs">258-555-0147</text>
      <text class="brand-name" x="470" y="-48" font-size="56" text-anchor="middle" textLength="420" lengthAdjust="spacingAndGlyphs">BRACKENVALE</text>
      <line class="rule" x1="300" y1="-30" x2="340" y2="-30"/>
      <text class="brand-sub" x="470" y="-22" font-size="24" text-anchor="middle" textLength="240" lengthAdjust="spacingAndGlyphs">GAS &amp; PLUMBING</text>
      <line class="rule" x1="600" y1="-30" x2="640" y2="-30"/>
      <text class="web-address" x="470" y="7" font-size="20" text-anchor="middle" textLength="340" lengthAdjust="spacingAndGlyphs">www.brackenvalegasplumbing.com</text>
    </g>
  </svg>

  <!-- Driver side, front to the left -->
  <svg class="wrap-panel wrap-panel--driver" viewBox="0 0 900 320" role="img" aria-label="Driver side van panel layout">
    <defs>
      <linearGradient id="orange-fade-driver" x1="0" y1="0" x2="0" y2="1">
        <stop offset="0" class="stop-top"/>
        <stop offset="1" class="stop-bottom"/>
      </linearGradient>
    </defs>
    <rect class="panel-body" x="0" y="0" width="900" height="320" rx="18"/>
    <path d="M0 260 L900 185 L900 302 Q900 320 882 320 L18 320 Q0 320 0 302 Z" fill="url(#orange-fade-driver)"/>
    <path class="band" d="M0 225 L900 150 L900 185 L0 260 Z"/>
    <g transform="translate(0 242.5) rotate(-4.76)">
      <text class="phone" x="610" y="-102" font-size="30" text-anchor="end" textLength="210" lengthAdjust="spacingAndGlyphs">258-555-0147</text>
      <text class="brand-name" x="420" y="-48" font-size="56" text-anchor="middle" textLength="420" lengthAdjust="spacingAndGlyphs">BRACKENVALE</text>
      <line class="rule" x1="250" y1="-30" x2="290" y2="-30"/>
      <text class="brand-sub" x="420" y="-22" font-size="24" text-anchor="middle" textLength="240" lengthAdjust="spacingAndGlyphs">GAS &amp; PLUMBING</text>
      <line class="rule" x1="550" y1="-30" x2="590" y2="-30"/>
      <text class="web-address" x="420" y="7" font-size="20" text-anchor="middle" textLength="340" lengthAdjust="spacingAndGlyphs">www.brackenvalegasplumbing.com</text>
      <circle class="brand-dot" cx="715" cy="-62" r="40"/>
    </g>
  </svg>

  <!-- Rear doors -->
  <svg class="wrap-panel wrap-panel--rear" viewBox="0 0 420 400" role="img" aria-label="Rear door panel layout">
    <defs>
      <linearGradient id="orange-fade-rear" x1="0" y1="0" x2="0" y2="1">
        <stop offset="0" class="stop-top"/>
        <stop offset="1" class="stop-bottom"/>
      </linearGradient>
    </defs>
    <rect class="panel-body" x="0" y="0" width="420" height="400" rx="18"/>
    <path d="M0 205 L420 205 L420 382 Q420 400 402 400 L18 400 Q0 400 0 382 Z" fill="url(#orange-fade-rear)"/>
    <rect class="band" x="0" y="170" width="420" height="35"/>
    <circle class="brand-dot" cx="62" cy="60" r="26"/>
    <text class="brand-name" x="100" y="70" font-size="32" textLength="250" lengthAdjust="spacingAndGlyphs">BRACKENVALE</text>
    <line class="rule" x1="118" y1="88" x2="140" y2="88"/>
    <text class="brand-sub" x="225" y="94" font-size="14" text-anchor="middle" textLength="140" lengthAdjust="spacingAndGlyphs">GAS &amp; PLUMBING</text>
    <line class="rule" x1="310" y1="88" x2="332" y2="88"/>
    <text class="phone" x="210" y="142" font-size="24" text-anchor="middle" textLength="170" lengthAdjust="spacingAndGlyphs">258-555-0147</text>
    <text class="web-address" x="210" y="193" font-size="14" text-anchor="middle" textLength="240" lengthAdjust="spacingAndGlyphs">www.brackenvalegasplumbing.com</text>
  </svg>
</div>
</body>
</html>
```